Label for packages of Pure Raw Natural Honeycomb

This is a label that will be used to sell pure raw honeycomb on the internet and in farm gate sales
Label must contain my Logo (which is attached)
my website www.hivelanterngold.ca
the weight 300 gr and the words Pure Raw Honeycomb
label design should fit onto a sticker 3" by 2" oval but If the size appears to small to get all that info on I am willing to look at a different size or shape

Target Market(s)

internet and in person farm gate customers

Industry/Entity Type

Agriculture

Font styles to use
Other font styles liked:
• the font should compliment my logo font

Colors
ffc214

Requirements
Must have
• Label must contain my Logo (attached) my website www.hivelanterngold.ca
• the weight 300 gr and the words Pure Raw Honeycomb would like something in black and gold with a bit of an Elegant vintage feel
Nice to have
• vintage feel
• If the size appears to small to get all that info on I am willing to look at a different size or shape
Should not have
• no cartoons

```html
<!DOCTYPE html>
<html lang="en">
<head>
<meta charset="utf-8">
<title>Pure Raw Honeycomb – Label</title>
<link rel="stylesheet" href="https://fonts.googleapis.com/css2?family=Playball&family=Italianno&family=Roboto+Condensed:wght@400;700&family=Arimo:wght@400&display=swap">
<style>
  :root {
    --ink: #000000;
    --label-black: #141414;
    --comb-dark: #1f1f1f;
    --rim-yellow: #f2e234;
    --gold: #ffc214;
    --gold-light: #f6ec4a;
    --gold-deep: #e3a80c;
    --script-gold: #e4d62c;
    --white: #ffffff;
    --backdrop: #eeeeee;
  }
  html, body {
    margin: 0;
    padding: 0;
    width: 1200px;
    height: 1068px;
    overflow: hidden;
    background: var(--backdrop);
  }
  .label {
    display: block;
    width: 1200px;
    height: 1068px;
  }
  .brand-name {
    font-family: "Roboto Condensed", sans-serif;
    font-weight: 700;
    font-size: 46px;
    fill: var(--white);
    letter-spacing: 1px;
  }
  .title-top {
    font-family: "Playball", cursive;
    font-size: 132px;
    fill: var(--script-gold);
  }
  .title-ribbon {
    font-family: "Italianno", cursive;
    font-size: 170px;
    fill: var(--ink);
    letter-spacing: 10px;
  }
  .weight {
    font-family: "Roboto Condensed", sans-serif;
    font-size: 52px;
    fill: var(--white);
  }
  .website {
    font-family: "Arimo", sans-serif;
    font-size: 31px;
    fill: var(--white);
  }
</style>
</head>
<body>
<svg class="label" viewBox="0 0 1200 1068" xmlns="http://www.w3.org/2000/svg">
  <defs>
    <linearGradient id="ribbon-gold" x1="0" y1="0" x2="1" y2="0">
      <stop offset="0" stop-color="var(--gold-deep)"/>
      <stop offset="0.25" stop-color="var(--gold-light)"/>
      <stop offset="0.6" stop-color="var(--gold)"/>
      <stop offset="1" stop-color="var(--gold-deep)"/>
    </linearGradient>
    <linearGradient id="tail-gold" x1="0" y1="0" x2="0" y2="1">
      <stop offset="0" stop-color="var(--gold-light)"/>
      <stop offset="1" stop-color="var(--gold)"/>
    </linearGradient>
  </defs>

  <!-- oval frame -->
  <g class="oval-frame">
    <ellipse cx="600" cy="534" rx="342" ry="446" fill="var(--ink)"/>
    <ellipse cx="600" cy="534" rx="330" ry="434" fill="var(--rim-yellow)"/>
    <ellipse cx="600" cy="534" rx="316" ry="420" fill="var(--label-black)"/>
    <ellipse class="comb-field" cx="600" cy="534" rx="308" ry="412" fill="var(--comb-dark)"
             role="img" aria-label="Faint honeycomb cell pattern with bees across the label background"/>
  </g>

  <!-- brand -->
  <g class="brand">
    <circle cx="600" cy="205" r="34" fill="none" stroke="var(--white)" stroke-width="5"/>
    <text class="brand-name" x="600" y="300" text-anchor="middle">Hive Lantern Gold</text>
  </g>

  <!-- title -->
  <text class="title-top" x="600" y="495" text-anchor="middle">Pure Raw</text>

  <!-- ribbon -->
  <g class="ribbon">
    <polygon class="ribbon-tail" points="285,585 160,595 222,650 175,722 300,705" fill="url(#tail-gold)"/>
    <polygon class="ribbon-tail" points="915,585 1040,595 978,650 1025,722 900,705" fill="url(#tail-gold)"/>
    <polygon class="ribbon-fold" points="270,672 300,705 300,672" fill="var(--gold-deep)"/>
    <polygon class="ribbon-fold" points="930,672 900,705 900,672" fill="var(--gold-deep)"/>
    <polygon class="ribbon-band" points="262,556 938,548 932,676 268,676" fill="url(#ribbon-gold)"/>
    <text class="title-ribbon" x="600" y="660" text-anchor="middle">Honeycomb</text>
  </g>

  <!-- details -->
  <text class="weight" x="600" y="770" text-anchor="middle">weight:300 gr</text>
  <text class="website" x="600" y="848" text-anchor="middle">www.hivelanterngold.ca</text>
</svg>
</body>
</html>
```